Home Design company focused on remodel and enhancement of kitchens and bathroorms

I already have a logo designed by ArtHarbor, I now need a design for my business cards.
The company is in the remodeling and enhancement industry for homes, focusing on kitchens and bathrooms, however, we can remodel or enhance every room in a home, an office space, etc.

The company's name is VELMOR HOME DESIGN, LLC

We'll focus on clients in the Rio Grande Valley, Texas. Primarily McAllen, Edinburg, Pharr, Mission, Brownsville and South Padre Island.

The design on the business card should transmit reliability, professionalism anda bit of upscale design.

The logo is in black and white, and would like to keep it that way.

The information that needs to be printed in the business cards is:
Company's name: Velmor Home Design
Company's Logo (attached)
My name: Noel Bramwit
Address, phone and email:
2715 N Parkline Road, Ste 348
Cedarbrook, OR 97990
(541) 555 0187
nbramwit@velmordesign.example
Website: velmordesign.example

```html
<!DOCTYPE html>
<html lang="en">
<head>
<meta charset="utf-8">
<title>Velmor Home Design — Business Cards</title>
<link rel="stylesheet" href="https://fonts.googleapis.com/css2?family=Montserrat:wght@300;400;700&display=swap">
<style>
  :root {
    --backdrop: #d6d6d6;
    --card-light: #ffffff;
    --card-dark: #2f2f2f;
    --ink: #111111;
    --ink-soft: #333333;
    --rule: #1a1a1a;
    --dark-mark: #1c1c1c;
    --dark-text: #8c8c8c;
  }
  * { box-sizing: border-box; margin: 0; padding: 0; }
  html, body {
    width: 1200px; height: 913px; overflow: hidden;
    background: var(--backdrop);
    font-family: "Montserrat", sans-serif;
  }
  .canvas { position: relative; width: 1200px; height: 913px; }

  .card {
    position: absolute;
    width: 540px; height: 309px;
    box-shadow: 0 14px 30px rgba(0,0,0,0.18);
    overflow: hidden;
  }
  .card--front { left: 40px; top: 150px; background: var(--card-light); }
  .card--back  { left: 620px; top: 454px; background: var(--card-dark); }

  /* brand lockup */
  .brand { position: absolute; display: flex; align-items: center; }
  .brand__square { width: 44px; height: 44px; border: 3px solid var(--ink); margin-right: 22px; }
  .brand__divider { width: 1px; height: 70px; background: var(--rule); margin-right: 14px; }
  .brand__name {
    font-weight: 400; font-size: 15px; letter-spacing: 0.38em;
    line-height: 1.15; text-transform: uppercase; color: var(--ink);
  }
  .card--front .brand { left: 40px; top: 36px; }

  .card--back .brand { left: 50%; top: 50%; transform: translate(-50%, -50%); }
  .card--back .brand__square { width: 62px; height: 62px; border-color: var(--dark-mark); margin-right: 30px; }
  .card--back .brand__divider { height: 96px; background: #555; margin-right: 18px; }
  .card--back .brand__name { color: var(--dark-text); font-size: 21px; }

  /* contact block */
  .contact { position: absolute; left: 40px; top: 134px; right: 30px; }
  .contact__group { display: flex; align-items: flex-start; margin-bottom: 10px; }
  .contact__rule { width: 34px; height: 1px; background: var(--rule); margin: 11px 18px 0 0; flex: none; }
  .person__name { font-weight: 700; font-size: 22px; color: var(--ink); line-height: 1.1; }
  .person__title { font-weight: 300; font-size: 12.5px; color: var(--ink-soft); margin-top: 3px; letter-spacing: 0.02em; }
  .details { list-style: none; }
  .details li {
    display: flex; align-items: center; font-weight: 300; font-size: 12.5px;
    color: var(--ink-soft); line-height: 1.35; margin-bottom: 2px;
  }
  .details svg { width: 12px; height: 12px; margin-right: 9px; flex: none; }
  .address { font-weight: 300; font-size: 12.5px; color: var(--ink-soft); line-height: 1.35; }
  .address span { display: block; }
</style>
</head>
<body>
<main class="canvas">

  <section class="card card--front" aria-label="Business card front">
    <div class="brand">
      <span class="brand__square" aria-hidden="true"></span>
      <span class="brand__divider" aria-hidden="true"></span>
      <p class="brand__name">Velmor<br>Home<br>Design</p>
    </div>

    <div class="contact">
      <div class="contact__group">
        <span class="contact__rule" aria-hidden="true"></span>
        <div>
          <h1 class="person__name">Noel Bramwit</h1>
          <p class="person__title">Managing Director</p>
        </div>
      </div>
      <div class="contact__group">
        <span class="contact__rule" aria-hidden="true"></span>
        <ul class="details">
          <li>
            <svg viewBox="0 0 12 12" aria-hidden="true"><path d="M3 1l2 2.5-1.2 1.2a6 6 0 0 0 3.5 3.5L8.5 7 11 9l-1.3 1.8C5.5 10.5 1.5 6.5 1.2 2.3z" fill="#222"/></svg>
            (541) 555 0187
          </li>
          <li>
            <svg viewBox="0 0 12 12" aria-hidden="true"><rect x="0.5" y="2" width="11" height="8" fill="#222"/><path d="M0.5 2l5.5 4.5L11.5 2" stroke="#fff" stroke-width="1" fill="none"/></svg>
            nbramwit@velmordesign.example
          </li>
          <li>
            <svg viewBox="0 0 12 12" aria-hidden="true"><circle cx="6" cy="6" r="5.2" fill="#222"/><path d="M1 6h10M6 0.8c-2.4 2.8-2.4 7.6 0 10.4M6 0.8c2.4 2.8 2.4 7.6 0 10.4" stroke="#fff" stroke-width="0.8" fill="none"/></svg>
            www.velmordesign.example
          </li>
        </ul>
      </div>
      <div class="contact__group">
        <span class="contact__rule" aria-hidden="true"></span>
        <p class="address"><span>2715 N Parkline Road, Ste 348</span><span>Cedarbrook, OR 97990</span></p>
      </div>
    </div>
  </section>

  <section class="card card--back" aria-label="Business card back">
    <div class="brand">
      <span class="brand__square" aria-hidden="true"></span>
      <span class="brand__divider" aria-hidden="true"></span>
      <p class="brand__name">Velmor<br>Home<br>Design</p>
    </div>
  </section>

</main>
</body>
</html>
```